Wedding Dried Apple Label / Name Place Card

We are looking for a simple but stylish label to be attached via string to a bag of dried apples from my family's fruit farm. The size of the label we think should be similar to the size of a business card. The packaging will be a plastic bag: 4" x 2" x 6".
We would like it to say something like:
Corin & Tessa
Est. Sept 10, 2017
Dried Apple Slices
Product of Marrow Orchard Farm
________________
(We need a spot to write in the name of the person and a table number)
Our colors are also grey and navy, and would like these colors to be used.
We have uploaded a photo of the plastic bag.

```html
<!DOCTYPE html>
<html lang="en">
<head>
<meta charset="utf-8">
<title>Corin &amp; Tessa – Dried Apple Label</title>
<link href="https://fonts.googleapis.com/css2?family=Great+Vibes&family=Cinzel:wght@400&family=Kaushan+Script&family=Roboto:wght@400&family=Roboto+Condensed:ital,wght@1,300&display=swap" rel="stylesheet">
<style>
  :root {
    --navy: #134468;
    --silver: #bccbd8;
    --edge: #e2e2e2;
    --white: #ffffff;
    --ink: #111111;
    --caption: #c8c8c8;
  }
  html, body {
    margin: 0;
    padding: 0;
    width: 1200px;
    height: 1200px;
    overflow: hidden;
    background: var(--white);
  }
  .label-sheet { display: block; width: 1200px; height: 1200px; }
  .apple-body { fill: var(--navy); stroke: var(--edge); stroke-width: 4; }
  .apple-stitch { fill: none; stroke: var(--white); stroke-width: 2.5; stroke-dasharray: 10 7; }
  .side-caption { font-family: "Roboto Condensed", sans-serif; font-style: italic; font-weight: 300; font-size: 62px; fill: var(--caption); }
  .couple-names { font-family: "Great Vibes", cursive; font-size: 68px; fill: var(--white); }
  .established { font-family: "Roboto", sans-serif; font-size: 22px; fill: var(--silver); }
  .product-title { font-family: "Cinzel", serif; font-size: 50px; fill: var(--white); }
  .farm-credit { font-family: "Roboto", sans-serif; font-size: 22px; fill: var(--white); }
  .field-heading { font-family: "Kaushan Script", cursive; font-size: 42px; fill: var(--white); }
  .field-box { fill: var(--silver); }
  .guest-name { font-family: "Great Vibes", cursive; font-size: 58px; fill: var(--ink); }
  .table-digit { font-family: "Great Vibes", cursive; font-size: 96px; fill: var(--ink); }
</style>
</head>
<body>
<svg class="label-sheet" viewBox="0 0 1500 1500" xmlns="http://www.w3.org/2000/svg">
  <defs>
    <path id="apple-outline" d="M380,95 L493,97 C460,140 452,200 462,245 C560,205 700,225 745,340 C790,460 765,570 705,670 C645,770 565,860 505,895 L462,900 C330,880 180,760 132,610 C95,480 115,360 220,272 C160,240 110,200 68,160 C160,100 300,85 378,180 Z"/>
    <linearGradient id="art-fill" x1="0" y1="0" x2="0" y2="1">
      <stop offset="0" stop-color="#2f5a7c"/>
      <stop offset="1" stop-color="#1c4c70"/>
    </linearGradient>
  </defs>

  <!-- front side -->
  <g class="label-front">
    <use href="#apple-outline" class="apple-body"/>
    <use href="#apple-outline" class="apple-stitch" transform="translate(440,500) scale(0.9) translate(-440,-500)"/>
    <text class="couple-names" x="442" y="370" text-anchor="middle">Corin&amp;Tessa</text>
    <text class="established" x="448" y="416" text-anchor="middle">Est. Sept 10, 2016</text>
    <text class="product-title" x="452" y="512" text-anchor="middle">DRIED</text>
    <text class="product-title" x="452" y="570" text-anchor="middle">APPLE SLICES</text>
    <text class="farm-credit" x="442" y="600" text-anchor="middle">Product of Marrow Orchard Farm</text>
    <rect role="img" aria-label="Line illustration of doves beside a nest on a leafy branch" x="338" y="632" width="236" height="160" rx="20" fill="url(#art-fill)"/>
    <text class="side-caption" x="590" y="185" text-anchor="middle">front</text>
  </g>

  <!-- back side -->
  <g class="label-back">
    <use href="#apple-outline" class="apple-body" transform="translate(1488,450) scale(-1,1)"/>
    <use href="#apple-outline" class="apple-stitch" transform="translate(1488,450) scale(-1,1) translate(440,500) scale(0.9) translate(-440,-500)"/>
    <text class="field-heading" x="1050" y="797" text-anchor="middle">surname</text>
    <rect class="field-box" x="847" y="830" width="386" height="95" rx="6"/>
    <text class="guest-name" x="1035" y="894" text-anchor="middle">Ms. Whitcombe</text>
    <text class="field-heading" x="1045" y="978" text-anchor="middle">table number</text>
    <circle class="field-box" cx="1040" cy="1060" r="60"/>
    <text class="table-digit" x="1036" y="1092" text-anchor="middle">5</text>
    <rect role="img" aria-label="Line illustration of grapevines with two wine glasses" x="910" y="1125" width="240" height="145" rx="20" fill="url(#art-fill)"/>
    <text class="side-caption" x="1275" y="502" text-anchor="middle">back</text>
  </g>
</svg>
</body>
</html>
```